CD Cover für junge Pop-Rock Band
Sehr kreative vorschläge. mehrere designs, die alle unter den top-favoriten für uns waren. änderungen und anpassungen stets schnell umgesetzt und auch nach gewinner-auswahl noch weiter zusammen gearbeitet bevor das endgültige design übergeben wurde.
Zielgruppe
Wir sind eine junge Band aus München und machen ausschließlich eigene Songs im Bereich Pop-Rock. Durch Einflüsse aus verschiedenen anderen Genres wie Funk, Reggae und Britpop grenzen sich unsere Songs von typischem Mainstream-Pop ab. Unsere Zielgruppe setzt sich aus Personen verschiedener Altersgruppen zusammen, der Fokus liegt jedoch auf Mitte Zwanzig- bis Mitte Dreißig-Jährigen.
Homepage: www.velvetmorrow.com
Chatterloop: www.chatterloop.net/velvetmorrowband
Aufgabenstellung
Wir benötigen ein Design für unsere neue EP "Paper Rivers". Diese wird in Form eines DigiPacks veröffentlicht werden. Daher werden Designs für Vorderseite, Rückseite, zwei Innenseiten sowie die CD selbst benötigt.
Folgendes sollte auf den jeweiligen Seiten enthalten sein:
Vorderseite:
- Bandschriftzug (siehe Anhang)
- Name der EP: Paper Rivers
Rückseite:
- Trackliste (1.Copper Kite, 2.Hold Us Near, 3.Birch Alley, 4.Can We Stay, 5.Quiet Hours)
- Credits (Recording by ..., Mix by ..., Mastering by ..., etc. -> wird noch festgesetzt)
Anmerkung:
Die roten Kratzer aus dem Bandlogo können bei Bedarf frei verwendet werden hinsichtlich Farbe, Muster, Gestaltung, Größe, etc.
Wir möchten keine Bilder von uns (z.B. von unserer Homepage, Chatterloop, etc) auf der CD.

```html
<!DOCTYPE html>
<html lang="de">
<head>
<meta charset="utf-8">
<title>Paper Rivers – Velvet Morrow</title>
<link rel="stylesheet" href="https://fonts.googleapis.com/css2?family=Josefin+Sans:wght@300;400;600;700&display=swap">
<style>
  :root {
    --backdrop: #eef0f1;
    --sleeve-dark: #141414;
    --sleeve-mid: #3a3a3a;
    --paper: #ffffff;
    --ink: #2b2b2b;
    --ink-soft: #6b6b6b;
    --accent: #c8171e;
    --white: #ffffff;
    --photo-light: #e7e7e6;
    --photo-mid: #b9b9b7;
  }
  * { margin: 0; padding: 0; box-sizing: border-box; }
  html, body {
    width: 1200px; height: 809px; overflow: hidden;
    background: var(--backdrop);
    font-family: "Josefin Sans", sans-serif;
  }
  .spread {
    position: absolute; left: 50px; top: 134px;
    display: flex; gap: 20px;
  }
  .panel {
    position: relative; width: 540px; height: 540px; overflow: hidden;
  }

  /* Front cover */
  .front-cover { background: var(--sleeve-dark); }
  .front-photo {
    position: absolute; inset: 0;
    background: radial-gradient(ellipse at 35% 35%, var(--sleeve-mid) 0%, #242424 45%, var(--sleeve-dark) 100%);
  }
  .ep-title {
    position: absolute; left: 0; right: 0; top: 180px;
    color: var(--white); font-weight: 300;
    font-size: 84px; line-height: 1; letter-spacing: 1px;
    text-transform: uppercase; white-space: nowrap;
  }
  .ep-title .line-one { display: block; padding-left: 70px; }
  .ep-title .line-two { display: block; padding-left: 140px; margin-top: 8px; }

  .band-name {
    position: absolute; display: flex; align-items: center; gap: 6px;
    font-weight: 600; text-transform: uppercase; letter-spacing: 0.5px;
    white-space: nowrap;
  }
  .band-name .mark { width: 14px; height: 14px; background: var(--accent); }
  .front-cover .band-name { left: 30px; bottom: 24px; color: var(--white); font-size: 19px; }

  /* Back cover */
  .back-cover { background: var(--paper); }
  .tracklist-heading {
    position: absolute; left: 34px; top: 52px;
    font-size: 36px; color: var(--ink); letter-spacing: 2px; text-transform: uppercase;
  }
  .tracklist-heading strong { font-weight: 700; }
  .tracklist-heading span { font-weight: 300; }
  .tracklist {
    position: absolute; left: 34px; top: 122px;
    list-style: none; display: grid;
    grid-template-columns: 150px 150px; column-gap: 16px;
    grid-template-rows: repeat(3, 22px);
    grid-auto-flow: column;
    font-size: 13px; font-weight: 300; color: var(--ink-soft);
    text-transform: uppercase; letter-spacing: 0.6px;
    white-space: nowrap;
  }
  .tracklist .num { color: var(--accent); font-weight: 600; margin-right: 4px; }
  .band-photo {
    position: absolute; left: 0; right: 0; bottom: 0; height: 300px;
    background: linear-gradient(180deg, var(--paper) 0%, var(--photo-light) 40%, var(--photo-mid) 100%);
  }
  .back-cover .band-name { right: 70px; bottom: 72px; color: var(--ink); font-size: 20px; }
</style>
</head>
<body>
  <main class="spread">
    <section class="panel front-cover">
      <div class="front-photo" role="img" aria-label="Dunkles Bühnenfoto einer Band beim Spielen"></div>
      <h1 class="ep-title"><span class="line-one">Paper</span><span class="line-two">Rivers</span></h1>
      <div class="band-name"><span class="mark"></span>Velvet Morrow</div>
    </section>

    <section class="panel back-cover">
      <h2 class="tracklist-heading"><strong>Track</strong><span>liste</span></h2>
      <ol class="tracklist">
        <li><span class="num">1.</span>Copper Kite</li>
        <li><span class="num">2.</span>Hold Us Near</li>
        <li><span class="num">3.</span>Birch Alley</li>
        <li><span class="num">4.</span>Can We Stay</li>
        <li><span class="num">5.</span>Quiet Hours</li>
      </ol>
      <div class="band-photo" role="img" aria-label="Gruppenfoto der vier Bandmitglieder vor hellem Hintergrund"></div>
      <div class="band-name"><span class="mark"></span>Velvet Morrow</div>
    </section>
  </main>
</body>
</html>
```